Visitenkarten-Design für Malermeisterbetrieb
Zielgruppe
Ich habe einen Malermeisterbetrieb und unsere Hauptaufgabe besteht im Fassadenanstrich, Fußbodenlegearbeiten und Tapezier- und Anstricharbeiten. Als Zielgruppe erreichen wir Verwaltungsfirmen, Privatkundschaft und Bauträger.
Aufgabenstellung
Visitenkarten bitte so ähnlich wie die alten Vorlagen (siehe Angang) bearbeiten aber die neuen Bilder (ebenfalls im Angang) einfügen

```html
<!DOCTYPE html>
<html lang="de">
<head>
<meta charset="utf-8">
<title>Visitenkarte Malermeisterbetrieb Jorben Kast</title>
<link rel="stylesheet" href="https://fonts.googleapis.com/css2?family=Great+Vibes&family=Open+Sans:wght@400;600;700&display=swap">
<style>
  :root {
    --stage: #e6e7e2;
    --card-light: #eef0c2;
    --card-mid: #dfe39a;
    --olive: #b3b83a;
    --olive-dark: #9ea22c;
    --ink: #1e1e1e;
    --script-red: #c8321e;
    --web-red: #c8321e;
    --stroke-orange: #f0b300;
    --stroke-orange-light: #f6c83a;
    --white: #ffffff;
  }
  * { margin: 0; padding: 0; box-sizing: border-box; }
  html, body { width: 1200px; height: 900px; overflow: hidden; }
  body {
    background: var(--stage);
    font-family: "Open Sans", Arial, sans-serif;
    color: var(--ink);
    position: relative;
  }
  .card {
    position: absolute;
    left: 290px;
    width: 620px;
    height: 354px;
    border-radius: 24px;
    overflow: hidden;
    background: linear-gradient(160deg, var(--card-light), var(--card-mid));
    box-shadow: 0 6px 18px rgba(0,0,0,.18);
  }
  .card--front { top: 70px; }
  .card--back { top: 476px; }
  .card__art { position: absolute; inset: 0; width: 100%; height: 100%; }

  /* front */
  .front__trade {
    position: absolute; top: 9px; right: 34px;
    font-weight: 700; font-size: 22px; letter-spacing: .2px;
  }
  .front__name {
    position: absolute; top: 50px; left: 238px;
    font-family: "Great Vibes", cursive;
    font-size: 66px; line-height: 1; color: var(--script-red);
  }
  .front__address {
    position: absolute; top: 160px; right: 70px;
    text-align: left; font-weight: 600; font-size: 15.5px; line-height: 1.3;
  }
  .front__phones {
    position: absolute; top: 202px; left: 160px;
    font-weight: 600; font-size: 15.5px; line-height: 1.3;
  }
  .front__mail {
    position: absolute; top: 278px; left: 26px;
    font-weight: 600; font-size: 15.5px;
  }
  .front__web {
    position: absolute; top: 302px; left: 26px;
    font-weight: 600; font-size: 21px; color: var(--web-red);
  }

  /* back */
  .services { position: absolute; left: 232px; top: 80px; list-style: none; }
  .service {
    position: relative;
    display: flex; align-items: baseline;
    height: 52px; margin-bottom: 18px;
    padding-left: 16px; padding-right: 26px;
    font-weight: 600; font-size: 19px;
  }
  .service__stroke {
    position: absolute; inset: 0;
    background: linear-gradient(90deg, var(--stroke-orange), var(--stroke-orange-light) 70%, var(--stroke-orange));
    border-radius: 6px 22px 22px 6px;
    z-index: 0;
  }
  .service__initial { position: relative; z-index: 1; font-size: 36px; font-weight: 700; line-height: 52px; }
  .service__rest { position: relative; z-index: 1; }
  .service:nth-child(1) { margin-left: 36px; width: 290px; }
  .service:nth-child(2) { margin-left: 18px; width: 320px; }
  .service:nth-child(3) { margin-left: 0; width: 350px; }
</style>
</head>
<body>

<section class="card card--front" aria-label="Vorderseite">
  <svg class="card__art" viewBox="0 0 620 354" aria-hidden="false">
    <defs>
      <linearGradient id="roomWarm" x1="0" y1="0" x2="1" y2="1">
        <stop offset="0" stop-color="#5b2a1c"/>
        <stop offset=".45" stop-color="#8a3b2b"/>
        <stop offset="1" stop-color="#cfc2aa"/>
      </linearGradient>
      <radialGradient id="frontSwoosh" cx=".6" cy=".7" r=".6">
        <stop offset="0" stop-color="#ffffff"/>
        <stop offset="1" stop-color="#ffffff" stop-opacity="0"/>
      </radialGradient>
    </defs>
    <path d="M200 354 Q 360 170 620 250 L620 354 Z" fill="url(#frontSwoosh)"/>
    <path d="M0 150 Q 320 110 620 300 L620 354 L0 354 Z" fill="#ffffff" opacity=".35"/>
    <rect x="0" y="0" width="620" height="44" fill="var(--olive)"/>
    <rect x="0" y="44" width="620" height="5" fill="var(--olive-dark)" opacity=".5"/>
    <g role="img" aria-label="Foto: Wohnraum mit roter Mustertapete, Holzvitrine und weißer Tür">
      <path d="M0 49 L250 49 Q 215 150 150 250 Q 120 270 0 270 Z" fill="url(#roomWarm)"/>
    </g>
  </svg>
  <div class="front__trade">Malermeisterbetrieb</div>
  <div class="front__name">Jorben Kast</div>
  <div class="front__address">Lindenweg 7<br>39418 Felsbach</div>
  <div class="front__phones">Tel.: 039201 457210<br>Fax: 039201 45722<br>Mobil: 01524883021</div>
  <div class="front__mail">E-Mail: jorbenkast@maler-kast.de</div>
  <div class="front__web">www.malermeister-kast.de</div>
</section>

<section class="card card--back" aria-label="Rückseite">
  <svg class="card__art" viewBox="0 0 620 354">
    <defs>
      <linearGradient id="roomCool" x1="0" y1="0" x2="1" y2="1">
        <stop offset="0" stop-color="#d9d9d4"/>
        <stop offset=".5" stop-color="#8e8f89"/>
        <stop offset="1" stop-color="#9a6a3c"/>
      </linearGradient>
      <linearGradient id="backSwoosh" x1="0" y1="0" x2="1" y2="0">
        <stop offset="0" stop-color="#ffffff" stop-opacity=".2"/>
        <stop offset="1" stop-color="#ffffff"/>
      </linearGradient>
    </defs>
    <path d="M280 40 Q 480 60 620 140 L620 330 Q 420 300 280 354 Z" fill="url(#backSwoosh)"/>
    <g role="img" aria-label="Foto: Flur mit grau gemusterter Tapete, Holzboden und Zimmerpflanze">
      <path d="M0 52 Q 170 20 330 40 Q 240 120 190 250 L0 250 Z" fill="url(#roomCool)"/>
    </g>
  </svg>
  <ul class="services">
    <li class="service"><span class="service__stroke"></span><span class="service__initial">F</span><span class="service__rest">assadenanstrich</span></li>
    <li class="service"><span class="service__stroke"></span><span class="service__initial">F</span><span class="service__rest">ußbodenlegearbeiten</span></li>
    <li class="service"><span class="service__stroke"></span><span class="service__initial">T</span><span class="service__rest">apezier - u.Anstricharbeiten</span></li>
  </ul>
</section>

</body>
</html>
```